KFL Noblesville Sign

I need to have a sign designed for a new self-storage facility we are going to be opening. The sign will be 4'W X 8'H.

Industry/Entity Type

Self Storage

Requirements
Must have
• Keystone Locker Hub logo at the top of the sign, under the logo I want the rendering.
• I also must have this information on the sign:
• 1. OPENING FALL 2016
• 2. Your premier self-storage facility.
• 3. www.keystonelockerhub.com

```html
<!DOCTYPE html>
<html lang="en">
<head>
<meta charset="utf-8">
<title>Keystone Locker Hub – Opening Sign</title>
<link rel="stylesheet" href="https://fonts.googleapis.com/css2?family=Roboto+Condensed:wght@300;400;700&display=swap">
<style>
  :root {
    --ink-black: #0b0b0b;
    --charcoal: #4a4a4a;
    --stripe-green: #2f8f3a;
    --stripe-green-dark: #1c6e2b;
    --brand-green: #2c7d38;
    --brand-yellow: #f6d21a;
    --panel-light: #f7f7f7;
    --panel-grey: #cfd0d2;
    --bronze-light: #b3925f;
    --bronze-dark: #8e6f43;
    --bronze-edge: #4a3016;
    --opening-brown: #3b2612;
    --white: #ffffff;
    --text-black: #111111;
  }
  html, body {
    margin: 0;
    padding: 0;
    overflow: hidden;
  }
  body {
    width: 1200px;
    height: 2400px;
    font-family: "Roboto Condensed", "Arial Narrow", sans-serif;
  }
  .sign {
    position: relative;
    width: 1200px;
    height: 2400px;
    overflow: hidden;
    background: radial-gradient(ellipse at 55% 45%, var(--panel-light) 0%, #e6e7e8 55%, var(--panel-grey) 100%);
  }
  .header-band {
    position: absolute;
    left: 0; top: 0;
    width: 1200px; height: 454px;
    background: linear-gradient(180deg, var(--charcoal) 0%, #1c1c1c 45%, var(--ink-black) 100%);
  }
  .header-stripe {
    position: absolute;
    left: 0; top: 454px;
    width: 1200px; height: 58px;
    background: linear-gradient(90deg, var(--stripe-green) 0%, var(--stripe-green-dark) 100%);
  }
  .brand-name {
    position: absolute;
    left: 266px; top: 30px;
    width: 668px; height: 400px;
    margin: 0;
    display: flex;
    flex-direction: column;
    justify-content: center;
    align-items: center;
    font-weight: 700;
    font-size: 124px;
    line-height: 1.02;
    color: var(--brand-yellow);
    text-align: center;
    letter-spacing: -1px;
  }
  .tagline {
    position: absolute;
    left: 72px; top: 820px;
    margin: 0;
    color: var(--brand-green);
    font-weight: 400;
  }
  .tagline .line-one {
    display: block;
    font-size: 108px;
    line-height: 1;
  }
  .tagline .soft {
    font-weight: 300;
    font-size: 76px;
  }
  .tagline .line-two {
    display: block;
    margin-left: 183px;
    margin-top: 6px;
    font-size: 108px;
    line-height: 1;
  }
  .tagline strong { font-weight: 700; }
  .tagline .tail { font-weight: 400; font-size: 80px; }
  .rendering {
    position: absolute;
    left: 0; top: 0;
    width: 1200px; height: 2400px;
  }
  .opening-banner {
    position: absolute;
    left: 258px; top: 1915px;
    width: 942px; height: 340px;
    background: linear-gradient(90deg, var(--bronze-light) 0%, #a88756 55%, var(--bronze-dark) 100%);
    border-left: 29px solid var(--bronze-edge);
    box-sizing: border-box;
    box-shadow: 0 10px 22px rgba(0,0,0,0.25);
  }
  .opening-label {
    position: absolute;
    left: 62px; top: 48px;
    margin: 0;
    font-weight: 400;
    font-size: 98px;
    line-height: 1;
    color: var(--opening-brown);
  }
  .opening-date {
    position: absolute;
    left: 56px; top: 142px;
    margin: 0;
    font-size: 186px;
    line-height: 1;
    color: var(--white);
    font-weight: 400;
    white-space: nowrap;
  }
  .opening-date strong { font-weight: 700; }
  .web-address {
    position: absolute;
    left: 0; top: 2296px;
    width: 1200px;
    margin: 0;
    padding-left: 270px;
    box-sizing: border-box;
    text-align: center;
    font-size: 64px;
    line-height: 1;
    color: var(--text-black);
    font-weight: 400;
  }
</style>
</head>
<body>
<main class="sign">
  <div class="header-band"></div>
  <div class="header-stripe"></div>

  <h1 class="brand-name">
    <span>Keystone</span>
    <span>Locker</span>
    <span>Hub</span>
  </h1>

  <p class="tagline">
    <span class="line-one"><span class="soft">Your </span><strong>Premier</strong></span>
    <span class="line-two"><strong>Self-Storage</strong> <span class="tail">facility</span></span>
  </p>

  <svg class="rendering" viewBox="0 0 1200 2400" xmlns="http://www.w3.org/2000/svg">
    <defs>
      <linearGradient id="frame-green" x1="0" y1="0" x2="1" y2="0">
        <stop offset="0" stop-color="#5fb548"/>
        <stop offset="1" stop-color="#1f6f2c"/>
      </linearGradient>
      <linearGradient id="scene-tones" x1="0" y1="0" x2="0" y2="1">
        <stop offset="0" stop-color="#c9ccc6"/>
        <stop offset="0.45" stop-color="#d9cdb6"/>
        <stop offset="0.72" stop-color="#c4b08e"/>
        <stop offset="0.85" stop-color="#9a9a52"/>
        <stop offset="1" stop-color="#7e8a3c"/>
      </linearGradient>
    </defs>
    <path class="rendering-frame"
          d="M1200 1330 L1200 1915 L560 1915 C250 1915 106 1720 106 1500 C106 1250 300 1096 520 1096 C650 1096 770 1140 1200 1330 Z"
          fill="url(#frame-green)"/>
    <path class="rendering-image" role="img"
          aria-label="Architectural rendering of the new two-storey self-storage building with green roll-up doors, a tree branch overhead and a lawn in front"
          d="M1200 1372 L1200 1915 L570 1915 C282 1915 134 1730 134 1505 C134 1278 318 1124 522 1124 C648 1124 760 1166 1200 1372 Z"
          fill="url(#scene-tones)"/>
  </svg>

  <section class="opening-banner">
    <p class="opening-label">OPENING</p>
    <p class="opening-date"><strong>FALL</strong> 2016</p>
  </section>

  <p class="web-address">www.keystonelockerhub.com</p>
</main>
</body>
</html>
```